Fishing charter business in Sitka Alaska needs new business card design

I have had the same design for 10 plus years, ready for something different. I have attached a copy of my current card and my website link is www.bluecoveangling.net
I am looking for something that will catch my clients eye, although I rely on word of mouth for most of my business a a nice business card will help people remember who I am. My business is located in Sitka Alaska, there are probably 20-30 other charter businesses in Sitka. I like the way my current card is laid out, with the two tone black and grey. I can leave it up to the designers to come up with something else.
Target Market(s)
men, women, couples. Anyone who likes fishing
Industry/Entity Type
Tourism
Contact Information for Business Card
Dorrance's Charter Service
Tidewater Rockline Sportfishing
Colors
Designer to choose colors to be used in the design.
Requirements
Must have
- Gilbert Dorrance
- PO Box 4716
- Sitka, AK 99835
- Compass Rose image
- 100 Ton USCG Licensed Captain
- gdorrance@wavelink.net
- 907-555-0142
- www.bluecoveangling.net
Nice to have
- ghost image of "boat helm"
Should not have
- be to complex

```html
<!DOCTYPE html>
<html lang="en">
<head>
<meta charset="utf-8">
<title>Dorrance's Charter Service – Business Card</title>
<link href="https://fonts.googleapis.com/css2?family=Bebas+Neue&family=Lato:wght@400;700&display=swap" rel="stylesheet">
<style>
  :root {
    --backdrop: #e9e4dc;
    --kraft-light: #cfab82;
    --kraft-dark: #b38a60;
    --ink: #121008;
    --rule: #5a4630;
  }
  * { margin: 0; padding: 0; box-sizing: border-box; }
  html, body { width: 1200px; height: 900px; overflow: hidden; }
  body { background: var(--backdrop); position: relative; font-family: "Lato", sans-serif; color: var(--ink); }

  .card {
    position: absolute;
    left: 330px;
    width: 558px;
    height: 344px;
    background: linear-gradient(135deg, var(--kraft-light), var(--kraft-dark));
  }
  .card--front { top: 90px; }
  .card--back { top: 469px; }

  .brand { position: absolute; top: 42px; left: 0; width: 100%; text-align: center; font-family: "Bebas Neue", sans-serif; line-height: 1; }
  .brand__name { font-size: 38px; letter-spacing: 0.5px; }
  .brand__tagline { font-size: 27px; letter-spacing: 0.3px; margin-top: 1px; }

  .captain { position: absolute; top: 146px; left: 0; width: 100%; text-align: center; }
  .captain__name { font-weight: 700; font-size: 17px; letter-spacing: 0.3px; }
  .captain__title { font-size: 15.5px; margin-top: 2px; }

  .icon-row { position: absolute; top: 193px; left: 188px; width: 180px; height: 20px; }

  .contact { position: absolute; top: 218px; left: 0; width: 100%; text-align: center; font-size: 15px; line-height: 20px; }

  .divider { position: absolute; top: 286px; left: 187px; width: 181px; height: 1px; background: var(--rule); }

  .address { position: absolute; top: 298px; left: 0; width: 100%; text-align: center; font-size: 15px; }

  .compass-rose {
    position: absolute; left: 170px; top: 58px; width: 220px; height: 230px;
    border-radius: 50%;
    background: radial-gradient(circle, rgba(18,16,8,0.45), rgba(18,16,8,0.12) 70%, rgba(18,16,8,0) 72%);
  }
</style>
</head>
<body>
  <section class="card card--front">
    <header class="brand">
      <div class="brand__name">Dorrance's Charter Service</div>
      <div class="brand__tagline">Tidewater Rockline Sportfishing</div>
    </header>

    <div class="captain">
      <div class="captain__name">GILBERT DORRANCE</div>
      <div class="captain__title">100 Ton USCG Licensed Captain</div>
    </div>

    <svg class="icon-row" viewBox="0 0 180 20" aria-hidden="true">
      <line x1="0" y1="10" x2="54" y2="10" stroke="#5a4630" stroke-width="1"/>
      <line x1="126" y1="10" x2="180" y2="10" stroke="#5a4630" stroke-width="1"/>
      <g fill="#121008">
        <circle cx="68" cy="10" r="9"/>
        <circle cx="90" cy="10" r="9"/>
        <circle cx="112" cy="10" r="9"/>
      </g>
      <g fill="#cfab82" stroke="none">
        <path d="M63 8.5 q5 -4 10 0 l-1.5 1.6 l-2 -1 v-1.2 q-1.5 -.6 -3 0 v1.2 l-2 1 z"/>
        <rect x="64.5" y="10.5" width="7" height="3.5" rx="1"/>
      </g>
      <g>
        <rect x="85" y="6.5" width="10" height="7" fill="#cfab82"/>
        <polyline points="85,6.5 90,10.5 95,6.5" fill="none" stroke="#121008" stroke-width="1"/>
      </g>
      <path d="M112 15 q-4 -4 -4 -6.5 a4 4 0 0 1 8 0 q0 2.5 -4 6.5 z" fill="#cfab82"/>
      <circle cx="112" cy="8.5" r="1.5" fill="#121008"/>
    </svg>

    <div class="contact">
      <div>907-555-0142</div>
      <div>gdorrance@wavelink.net</div>
      <div>www.bluecoveangling.net</div>
    </div>

    <div class="divider"></div>

    <div class="address">PO Box 4716, Sitka, AK 99835</div>
  </section>

  <section class="card card--back">
    <div class="compass-rose" role="img" aria-label="Hand-drawn compass rose with N, E, S, W points"></div>
  </section>
</body>
</html>
```